Co-Living Retreat Centre Pitch Deck

We are needing fresh new pitch deck for our Co-Living Retreat Centre project. We are building a 40 unit community focused on personal development and holistic living!

Here is the branding guide:
https://www.plorvex.com/design/QWRT8mVbnk3/pzLoHyRdf_4sM7T-9wQxRe/edit

Here is the Content:
https://files.trumbelo.net/drive/folders/7Kq4Xv9RmTb2yN51wPcLhZ8dF3sJe0Ua?usp=sharing

Target Market(s)

30-45 Year olds that are into Yoga, Meditation, Personal Development, Balance Lifestyle.

Font styles to use
Serif
Sans Serif

Requirements
Must have
• Must have the colours from our branding.
Nice to have
• Have some elements of nature, Inspiration,

```html
<!DOCTYPE html>
<html lang="en">
<head>
<meta charset="utf-8">
<title>The Quiet Grove – Pitch Deck Slides</title>
<link href="https://fonts.googleapis.com/css2?family=Montserrat:wght@300;400;500;600;700&display=swap" rel="stylesheet">
<style>
  :root {
    --canvas: #efefef;
    --sage: #5a7d5f;
    --sage-band: #52735a;
    --sage-deep: #3e5c47;
    --gold: #c8940a;
    --gold-band: #c28f09;
    --white: #ffffff;
    --ink: #000000;
  }
  * { margin: 0; padding: 0; box-sizing: border-box; }
  html, body { width: 1200px; height: 1200px; overflow: hidden; }
  body {
    background: var(--canvas);
    font-family: 'Montserrat', sans-serif;
    color: var(--white);
    position: relative;
  }
  .slide { position: absolute; overflow: hidden; }
  .slide--sage { background: var(--sage); }
  .slide--gold { background: var(--gold); }
  .band { position: absolute; }
  .slide--sage .band { background: var(--sage-band); }
  .slide--gold .band { background: var(--gold-band); }
  .page-no { position: absolute; font-weight: 600; font-size: 13px; letter-spacing: -0.3px; }
  .page-no--gold { color: var(--gold); }
  .title { position: absolute; font-weight: 300; white-space: nowrap; }
  .title b { font-weight: 700; }
  .centered { left: 0; right: 0; text-align: center; }

  /* team */
  .team-slide { left: 11px; top: 152px; width: 777px; height: 437px; }
  .team-slide .band { left: 0; top: 89px; width: 777px; height: 316px; }
  .team-slide .page-no { left: 630px; top: 48px; font-size: 24px; }
  .team-slide .title { top: 108px; font-size: 33px; }
  .team-member { position: absolute; top: 161px; width: 70px; text-align: center; }
  .portrait { width: 70px; height: 157px; }
  .member-name { margin-top: 12px; font-weight: 600; font-size: 13px; line-height: 17px; width: 90px; margin-left: -10px; }
  .member-role { font-weight: 400; font-size: 13px; line-height: 17px; width: 100px; margin-left: -15px; }

  /* bio */
  .bio-slide { left: 811px; top: 140px; width: 378px; height: 212px; }
  .bio-slide .band { left: 42px; top: 0; width: 295px; height: 212px; }
  .bio-slide .page-no { left: 55px; top: 18px; font-size: 12px; }
  .bio-slide .title { left: 55px; top: 48px; font-size: 17px; }
  .bio-text { position: absolute; left: 55px; top: 75px; width: 95px; font-size: 4.6px; line-height: 6.6px; }
  .bio-text p + p { margin-top: 6px; }
  .bio-portrait { position: absolute; left: 180px; top: 28px; width: 132px; height: 160px; background: var(--sage-deep); }

  /* section slides */
  .section { width: 378px; height: 212px; }
  .section .band { left: 0; top: 43px; width: 378px; height: 152px; }
  .section .page-no { left: 306px; top: 19px; }
  .section .title { top: 98px; font-size: 20px; }
  .amount { position: absolute; top: 114px; font-weight: 700; font-size: 24px; }

  .s14 { left: 811px; top: 378px; }
  .s18 { left: 11px; top: 617px; }
  .s17 { left: 411px; top: 617px; }
  .s15 { left: 811px; top: 617px; }
  .s20 { left: 11px; top: 854px; }
  .s18b { left: 411px; top: 854px; }
  .s16 { left: 811px; top: 854px; }

  .s14 .title { top: 98px; }
  .s18 .title, .s15 .title { top: 85px; }
  .s18 .page-no { left: 310px; }
  .s17 .page-no { left: 40px; }
  .s16 .title { top: 90px; }

  .legal-col { position: absolute; top: 57px; width: 88px; font-size: 5.6px; line-height: 8.3px; }
  .legal-col--left { left: 42px; }
  .legal-col--right { left: 250px; }
  .s17 .title { left: 135px; top: 90px; width: 110px; text-align: center; font-size: 20px; }

  .s20 .band { display: none; }
  .s20 .page-no { left: 40px; top: 26px; }
  .s20 .title { left: 0; width: 378px; text-align: center; top: 30px; font-size: 20px; }
  .purpose-text { position: absolute; left: 60px; top: 66px; width: 260px; text-align: center; font-weight: 600; font-size: 6.9px; line-height: 10.5px; }

  .s18b .band { left: 26px; top: 0; width: 326px; height: 212px; }
  .s18b .page-no { left: 216px; top: 19px; }
  .round-label { position: absolute; color: var(--gold); font-size: 10px; font-weight: 300; }
  .round-label b { font-weight: 700; }
  .round-text { position: absolute; font-size: 4.8px; line-height: 6.6px; width: 75px; }
  .round-text p + p { margin-top: 6px; }
  .funding-box { position: absolute; left: 134px; top: 36px; width: 109px; height: 71px; border: 0.8px solid var(--white); text-align: center; padding-top: 16px; font-size: 19px; line-height: 16px; }
  .funding-box span { display: block; font-weight: 300; }
  .funding-box b { display: block; font-weight: 700; }
  .funding-note { position: absolute; left: 130px; top: 122px; width: 118px; text-align: center; font-weight: 600; font-size: 6.6px; line-height: 10.5px; }
</style>
</head>
<body>

<section class="slide slide--sage team-slide">
  <div class="band"></div>
  <div class="page-no page-no--gold">&gt;&gt;12</div>
  <h1 class="title centered"><b>meet</b>the<b>team</b></h1>
  <div class="team-member" style="left:42px"><div class="portrait" role="img" aria-label="Portrait of Dario" style="background:var(--ink)"></div><div class="member-name">Dario</div><div class="member-role">Founder</div></div>
  <div class="team-member" style="left:131px"><div class="portrait" role="img" aria-label="Portrait of Ravi" style="background:linear-gradient(#6b7a4a,#7a6a8a)"></div><div class="member-name">Ravi</div><div class="member-role">Operations Director</div></div>
  <div class="team-member" style="left:221px"><div class="portrait" role="img" aria-label="Portrait of Milena" style="background:var(--ink)"></div><div class="member-name">Milena</div><div class="member-role">Event/Retreat Manager</div></div>
  <div class="team-member" style="left:311px"><div class="portrait" role="img" aria-label="Portrait of Teo" style="background:linear-gradient(#b8b8b8,#2a2a2a)"></div><div class="member-name">Teo</div><div class="member-role">Financial Officer</div></div>
  <div class="team-member" style="left:401px"><div class="portrait" role="img" aria-label="Portrait of Lorna" style="background:var(--ink)"></div><div class="member-name">Lorna</div><div class="member-role">Branding/ Design</div></div>
  <div class="team-member" style="left:491px"><div class="portrait" role="img" aria-label="Portrait of Nadia" style="background:linear-gradient(#e8e4e0,#1e1a1a)"></div><div class="member-name">Nadia</div><div class="member-role">Architect</div></div>
  <div class="team-member" style="left:581px"><div class="portrait" role="img" aria-label="Portrait of Sella" style="background:linear-gradient(#8e9274,#c9a890)"></div><div class="member-name">Sella</div><div class="member-role">Landscaping/ Permaculture</div></div>
  <div class="team-member" style="left:670px"><div class="portrait" role="img" aria-label="Portrait of Arlo" style="background:var(--ink)"></div><div class="member-name">Arlo</div><div class="member-role">General Contractor</div></div>
</section>

<section class="slide slide--sage bio-slide">
  <div class="band"></div>
  <div class="page-no page-no--gold">&gt;&gt;11</div>
  <h2 class="title">dario<b>venholm</b></h2>
  <div class="bio-text">
    <p>After travelling for 15 years in over 75 countries, Dario has chosen to settle down in Bali to create and build The Quiet Grove.</p>
    <p>He has 13 years of experience running a well-established travel company that comprises many different lifestyle brands including a co-living company and a small hotel in Thailand. Generating 8 figures of revenue over the last decade.</p>
    <p>Now he is shifting his focus to create a more balanced lifestyle fueled by his passion for personal development and positive impact in the world.</p>
  </div>
  <div class="bio-portrait" role="img" aria-label="Portrait of Dario Venholm"></div>
</section>

<section class="slide slide--gold section s14">
  <div class="band"></div>
  <div class="page-no">&gt;&gt;14</div>
  <h2 class="title centered">market<b>trends</b></h2>
</section>

<section class="slide slide--gold section s18">
  <div class="band"></div>
  <div class="page-no">&gt;&gt;18</div>
  <h2 class="title centered"><b>use</b>of<b>funds</b></h2>
  <div class="amount centered" style="text-align:center">$ 3,500,000 USD</div>
</section>

<section class="slide slide--sage section s17">
  <div class="band"></div>
  <div class="page-no">&gt;&gt;17</div>
  <p class="legal-col legal-col--left">We have 2 corporate entities set up in order to create a secure legal structure with blockchain technology for our ownership structure. Our main company is located in the Seychelles which holds the tokens. This company owns our Indonsian company that will own the leasehold property. This creates extra security for our investors and has tax advantages.</p>
  <h2 class="title">the<b>legal</b></h2>
  <p class="legal-col legal-col--right">We have two corporate entities set up simultaneously in order to create a secure legal structure that uses blockchain technology for our ownership framework. Our main company is located in the Seychelles which holds the crypto tokens. This company owns our Indonsian company that will possess the leasehold property. This model creates extra security for our investors and comes with tax advantages.</p>
</section>

<section class="slide slide--gold section s15">
  <div class="band"></div>
  <div class="page-no">&gt;&gt;15</div>
  <h2 class="title centered">financial<b>model</b></h2>
  <div class="amount centered" style="text-align:center">$ 100,000 USD</div>
</section>

<section class="slide slide--sage section s20">
  <div class="band"></div>
  <div class="page-no">&gt;&gt;20</div>
  <h2 class="title">the<b>purpose</b></h2>
  <p class="purpose-text">We are becoming aware of<br>the need to change the way we live.<br>Here at The Quiet Grove we exist to<br>empower a new wave of reality in<br>spaces that are part of the solution<br>not the problem.<br>A future-focused community<br>that stimulates the co-existence of<br>nature and optimal living. Focusing<br>on human connection,<br>personal growth and impact.</p>
</section>

<section class="slide slide--sage section s18b">
  <div class="band"></div>
  <div class="round-label" style="left:37px;top:17px">round<b>one</b></div>
  <div class="round-text" style="left:37px;top:36px"><p>Friends, Family &amp; Partners will get the first opportunity to invest in Hollow Oak before more institutional investment comes in.</p></div>
  <div class="round-label" style="left:37px;top:79px">round<b>three</b></div>
  <div class="round-text" style="left:37px;top:98px">
    <p>Community members can buy shares from investors transitioning ownership back to the community. At 15% more to cover the investors interest rates.</p>
    <p>Community members can buy back shares from investors transitioning ownership back to the community.</p>
  </div>
  <div class="page-no">&gt;&gt;18</div>
  <div class="funding-box"><span>funding</span><b>strategy</b></div>
  <p class="funding-note">All shareholders will obtain access to the spaces based on the amount they invest. Everything is 100% transparent and evenly distributed, using our tokenized system.</p>
  <div class="round-label" style="left:292px;top:17px">round<b>two</b></div>
  <div class="round-text" style="left:260px;top:36px;width:86px">
    <p>Institutional Investment will have the opportunity to invest with a clear buyback model from the community, buying back shares from investors that provide a 15% rate of return. If payback does not come in, investors will still have ownership of the property ensuring it is a safe investment for all.</p>
    <p>Institutional Investment will have the opportunity to invest with a clear buyback model from the community that provides investors with a 15% rate of return. If payback does not come in, investors will still have ownership of the property ensuring it is a safe investment for all.</p>
    <p>If payback does not come in, investment is still secured by a stake in the property ensuring a safe investment for investors.</p>
  </div>
</section>

<section class="slide slide--sage section s16">
  <div class="band"></div>
  <div class="page-no">&gt;&gt;16</div>
  <h2 class="title centered">the<b>governance</b></h2>
</section>

</body>
</html>
```